Maple Crest Branding for Contracts and Customer facing documents

We are hoping to create a themed branding for our company. We would like to leverage this across our contracts, documents, and all client information and proposals. www.HomesByMapleCrest.example is our website. We are selling high end custom homes. We am intending to use this template for a Lead Magnet and other marketing.

Target Market(s)

Luxury Custom Home Buyers

Industry/Entity Type

Residential Construction

Other font styles liked:
• You may choose, We want to be elegant but very legible and professional

Colors
0054AA
0677BA
7BADD7
CADEEF
E8F1F8

```html
<!DOCTYPE html>
<html lang="en">
<head>
<meta charset="utf-8">
<title>Maple Crest – Brochure Pages</title>
<link href="https://fonts.googleapis.com/css2?family=Poppins:ital,wght@0,300;0,400;0,500;0,600;0,700;0,800;1,400;1,600&family=Fira+Sans:ital,wght@1,600;1,800;1,900&family=Jost:wght@400&family=Roboto+Condensed:wght@500&display=swap" rel="stylesheet">
<style>
:root{
  --backdrop:#3b3b3b;
  --paper:#ffffff;
  --teal:#6a8b96;
  --teal-dark:#55737e;
  --ink:#1c1c1c;
  --body:#555555;
  --accent:#cf9463;
  --accent-block:#d59c6c;
  --mint:#9fd39b;
  --logo-panel:#f1f1f2;
}
*{margin:0;padding:0;box-sizing:border-box}
html,body{width:909px;height:1200px;overflow:hidden;background:var(--backdrop)}
body{position:relative;font-family:"Poppins",sans-serif}
.page{position:absolute;width:380px;height:532px;background:var(--paper);overflow:hidden}
.page--cover{left:61px;top:54px}
.page--connect{left:469px;top:54px}
.page--different{left:61px;top:616px}
.page--ideas{left:469px;top:616px}
.abs{position:absolute}
.photo{position:absolute}

/* cover */
.cover-band{left:0;top:235px;width:380px;height:187px;background:var(--teal)}
.cover-mint{left:-1px;top:280px;width:28px;height:98px;background:var(--mint);border:1.5px solid #fff;border-left:none}
.cover-line{font-family:"Fira Sans",sans-serif;font-style:italic;right:23px;text-align:right;white-space:nowrap}
.cover-lux{top:252px;font-weight:600;font-size:26px;color:#fff}
.cover-home{top:284px;font-weight:900;font-size:43px;color:var(--ink);letter-spacing:-.3px}
.cover-area-box{left:112px;top:340px;width:245px;height:37px;background:var(--teal-dark)}
.cover-area{left:0;width:245px;top:2px;text-align:center;font-family:"Fira Sans",sans-serif;font-style:italic;font-weight:800;font-size:25px;color:#fff;white-space:nowrap}
.cover-tag{top:385px;font-weight:600;font-size:11px;color:var(--ink)}
.cover-web{left:30px;top:476px;font-family:"Poppins",sans-serif;font-style:italic;font-size:7.4px;letter-spacing:1.3px;color:var(--ink);white-space:nowrap}
.cover-web b{color:var(--accent);font-weight:400}
.logo-panel{left:211px;top:427px;width:169px;height:105px;background:var(--logo-panel)}
.brand{position:absolute;left:0;width:169px;top:42px;display:flex;align-items:center;justify-content:center;gap:6px;font-family:"Poppins",sans-serif;font-weight:500;font-size:14px;color:var(--ink)}
.brand i{display:block;width:9px;height:9px;background:var(--ink)}

/* connect */
.connect-head{left:0;top:0;width:380px;height:146px;background:var(--teal)}
.quote-mark{left:21px;top:22px;width:46px;height:36px}
.quote-rule{left:81px;top:57px;width:139px;height:1px;background:#fff}
.connect-title{left:22px;top:70px;font-weight:800;font-size:17px;line-height:19.5px;color:var(--ink);white-space:nowrap}
.connect-lede{left:23px;top:113px;width:345px;font-size:8.4px;line-height:10px;color:#fff;font-weight:400}
.sec-title{font-weight:400;color:#2a2a2a;white-space:nowrap}
.sec-title b{color:var(--accent);font-weight:600}
.rule{position:absolute;height:1px;background:#cfcfcf}
.about-title{left:191px;top:166px;font-size:18.5px}
.about-col{left:191px;top:194px;width:172px;display:flex;flex-direction:column;gap:6px}
.about-sub{font-weight:600;font-size:7.9px;line-height:10px;color:var(--accent)}
.small-copy{font-size:6.3px;line-height:9.2px;color:var(--body)}
.about-copy p+p{margin-top:9px}
.mission-title{left:21px;top:373px;font-size:15.5px}
.mission-copy{left:21px;top:401px;width:137px;line-height:8.7px}
.folio{position:absolute;display:flex;align-items:center;gap:3px;font-size:8.6px;color:var(--accent)}
.folio i{display:block;width:137px;height:1px;background:#333}

/* different */
.diff-title{left:30px;top:21px;font-size:16.5px}
.diff-copy{left:30px;top:57px;width:324px;font-size:7px;line-height:10.5px;color:var(--body)}
.checks{left:30px;top:103px;list-style:none}
.checks li{display:flex;align-items:center;gap:5px;height:19.2px;font-size:7px;color:var(--ink);white-space:nowrap}
.checks svg{width:10px;height:10px;flex:none}
.diff-band{left:0;top:301px;width:380px;height:187px;background:var(--teal)}
.frame{position:absolute;background:#fff}
.diff-quote{left:21px;top:427px;width:339px;border-left:1.6px solid var(--accent);padding-left:6px;font-style:italic;font-size:7.5px;line-height:9.9px;color:#fff;text-align:justify}

/* ideas */
.ideas-title{left:28px;top:21px;font-size:15.8px}
.ideas-copy{left:28px;top:56px;width:169px;font-size:6.7px;line-height:9.9px;color:var(--body);text-align:justify}
.ideas-copy p+p{margin-top:10px}
.orange-block{left:0;top:339px;width:161px;height:145px;background:var(--accent-block)}
.teal-block-a{left:168px;top:355px;width:212px;height:129px;background:var(--teal)}
.teal-block-b{left:203px;top:260px;width:177px;height:100px;background:var(--teal)}
.services{left:28px;top:379px;width:110px;list-style:none}
.services li{font-family:"Roboto Condensed",sans-serif;font-weight:500;font-size:10.3px;color:#fff;height:33px;position:relative;white-space:nowrap}
.services li.has-rule::after{content:"";position:absolute;left:0;top:21px;width:107px;height:1px;background:#fff}
.services li.has-rule::before{content:"";position:absolute;left:105px;top:19px;width:4px;height:4px;border-radius:50%;background:#fff}
.ideas-quote{left:219px;top:277px;width:128px;font-family:"Jost",sans-serif;font-size:12px;line-height:14.9px;color:#fff}
</style>
</head>
<body>

<!-- Cover -->
<section class="page page--cover">
  <div class="photo" style="left:0;top:0;width:380px;height:231px;background:linear-gradient(180deg,#9fb8cf 0%,#8a8a78 30%,#5f6370 55%,#7c8f5c 80%,#7ea04c 100%)" role="img" aria-label="Photo of a large grey-sided luxury lake house with stone base and wraparound deck among trees"></div>
  <div class="abs cover-band"></div>
  <div class="abs cover-mint"></div>
  <div class="abs cover-line cover-lux">Luxury Custom</div>
  <div class="abs cover-line cover-home">Home Builder in</div>
  <div class="abs cover-area-box"><div class="abs cover-area">Charlottesville Area</div></div>
  <div class="abs cover-line cover-tag">Build with the best, Build With Maple Crest</div>
  <div class="abs cover-web">www.<b>homesbymaplecrest</b>.example</div>
  <div class="abs logo-panel"><div class="brand"><i></i>Maple Crest</div></div>
</section>

<!-- Page 02 -->
<section class="page page--connect">
  <div class="abs connect-head"></div>
  <svg class="abs quote-mark" viewBox="0 0 46 36" aria-hidden="true">
    <path d="M1 35V17C1 8 5 2 14 1l2 5c-5 1-7 5-7 10h11v19Z" fill="none" stroke="#fff" stroke-width="1.2"/>
    <path d="M25 35V17C25 8 29 2 38 1l2 5c-5 1-7 5-7 10h11v19Z" fill="none" stroke="#fff" stroke-width="1.2"/>
  </svg>
  <div class="abs quote-rule"></div>
  <h2 class="abs connect-title">How We Connect With<br>Our Clients</h2>
  <p class="abs connect-lede">Maple Crest ensures a very personal home building experience guaranteeing our utmost attention to detail that you deserve as a customer.</p>

  <div class="photo" style="left:0;top:152px;width:176px;height:206px;background:linear-gradient(100deg,#3b2b26 0%,#9a5a48 35%,#b56e5a 55%,#e9e6df 75%,#3a3f6b 100%)" role="img" aria-label="Photo of the brick office storefront with black shutters and a hanging sign"></div>
  <h2 class="abs sec-title about-title">About <b>Us</b></h2>
  <div class="rule" style="left:191px;top:190px;width:162px"></div>
  <div class="abs about-col">
    <p class="about-sub">“Maple Crest” – a name to found a business on, or more importantly, a life on.</p>
    <div class="small-copy about-copy">
      <p>Maple Crest has a long history with its inception in the year 2009. Growing up in the construction industry and family business, the groundworks were set in motion at an early age.</p>
      <p>We have discovered that doing what we love makes our job both enjoyable and satisfying. We are absolutely passionate about the entire home building process; from the first scheduled meeting, through the design process, during the construction phase, and eventually handing over the keys to your beautiful new home.</p>
    </div>
  </div>

  <h2 class="abs sec-title mission-title">Our <b>Mission</b></h2>
  <div class="rule" style="left:21px;top:396px;width:136px"></div>
  <p class="abs small-copy mission-copy">We partner with each one of our customers to design and construct a home that integrates your lifestyle with a comfortable living environment. Our process is driven by a combination of lifestyle, architectural detail, and budget. Maple Crest will work diligently to focus on what is important to you as our customer. We promise that our high standards will not be compromised in attaining our collective goals.</p>
  <div class="photo" style="left:176px;top:358px;width:204px;height:136px;background:linear-gradient(160deg,#2a1c18 0%,#3a2a24 20%,#e4e6ea 45%,#dfe2e6 70%,#5d7a45 90%,#2a1c18 100%)" role="img" aria-label="Photo of a monitor showing a floor plan and a 3D rendering of a house"></div>
  <div class="folio" style="left:186px;top:506px"><i></i>Page : 02</div>
</section>

<!-- Page 03 -->
<section class="page page--different">
  <h2 class="abs sec-title diff-title">Intentionally <b>Different.</b></h2>
  <div class="rule" style="left:30px;top:47px;width:287px"></div>
  <p class="abs diff-copy">Maple Crest is the best luxury custom home builder in Virginia whose focus is to construct high quality, energy efficient luxury custom homes in Charlottesville, and surrounding areas. Because we are family owned, our values are founded on a cooperative approach relating to the building experience. At Maple Crest we focus on the customer’s priorities on every custom home we build.</p>
  <ul class="abs checks">
    <li><svg viewBox="0 0 10 10"><rect x=".5" y="1.5" width="8" height="8" fill="none" stroke="#555" stroke-width=".8"/><path d="M2.3 5.2l2 2.3L9.5.6" fill="none" stroke="#cf9463" stroke-width="1.2"/></svg>Dedicated And Caring Team-approach To Custom Home Building</li>
    <li><svg viewBox="0 0 10 10"><rect x=".5" y="1.5" width="8" height="8" fill="none" stroke="#555" stroke-width=".8"/><path d="M2.3 5.2l2 2.3L9.5.6" fill="none" stroke="#cf9463" stroke-width="1.2"/></svg>Long-term Trade Partners, Suppliers, Banks And Lender Relationships</li>
    <li><svg viewBox="0 0 10 10"><rect x=".5" y="1.5" width="8" height="8" fill="none" stroke="#555" stroke-width=".8"/><path d="M2.3 5.2l2 2.3L9.5.6" fill="none" stroke="#cf9463" stroke-width="1.2"/></svg>In-house Design Capability</li>
    <li><svg viewBox="0 0 10 10"><rect x=".5" y="1.5" width="8" height="8" fill="none" stroke="#555" stroke-width=".8"/><path d="M2.3 5.2l2 2.3L9.5.6" fill="none" stroke="#cf9463" stroke-width="1.2"/></svg>Our Standards Are Other Builders’ Options</li>
    <li><svg viewBox="0 0 10 10"><rect x=".5" y="1.5" width="8" height="8" fill="none" stroke="#555" stroke-width=".8"/><path d="M2.3 5.2l2 2.3L9.5.6" fill="none" stroke="#cf9463" stroke-width="1.2"/></svg>Weekly Communication During The Home Building Process</li>
    <li><svg viewBox="0 0 10 10"><rect x=".5" y="1.5" width="8" height="8" fill="none" stroke="#555" stroke-width=".8"/><path d="M2.3 5.2l2 2.3L9.5.6" fill="none" stroke="#cf9463" stroke-width="1.2"/></svg>Customer Referral Program</li>
  </ul>
  <div class="abs diff-band"></div>
  <div class="frame" style="left:30px;top:227px;width:150px;height:187px"></div>
  <div class="photo" style="left:39px;top:232px;width:133px;height:175px;background:linear-gradient(170deg,#f4f4f2 0%,#e8e6e2 40%,#8a8580 55%,#eceae6 70%,#d8d8d6 100%)" role="img" aria-label="Photo of a bright white kitchen with crystal pendant lights and a marble island"></div>
  <div class="frame" style="left:195px;top:200px;width:150px;height:134px"></div>
  <div class="photo" style="left:204px;top:205px;width:133px;height:121px;background:linear-gradient(135deg,#e9ecef 0%,#dadde0 40%,#c9b89a 60%,#4b5a78 80%,#e0e2e4 100%)" role="img" aria-label="Photo of a carpenter cutting trim with a miter saw inside a new home"></div>
  <div class="frame" style="left:195px;top:348px;width:150px;height:66px"></div>
  <div class="photo" style="left:204px;top:354px;width:133px;height:54px;background:linear-gradient(180deg,#efeeec 0%,#7a5a3e 35%,#5e432d 70%,#caa98a 100%)" role="img" aria-label="Photo of a kitchen with rich wood cabinetry and a large island"></div>
  <p class="abs diff-quote">We are the best at what we do and we can prove it! Our company always interacts with integrity, honesty, and customer satisfaction as our primary focus threfore we are confident you will feel these values in our very first interaction together and thereafter. Maple Crest is the best luxury custom home builder that leads by serving others. We are your trusted custom home builder in Charlottesville VA and surrounding areas.</p>
  <div class="folio" style="left:21px;top:504px">Page : 03<i></i></div>
</section>

<!-- Page 04 -->
<section class="page page--ideas">
  <h2 class="abs sec-title ideas-title">We Bring <b>Ideas Home</b></h2>
  <div class="rule" style="left:28px;top:47px;width:169px"></div>
  <div class="abs ideas-copy">
    <p>A luxury custom home builder that does it all : from planning and design to architecture and execution, it all happens here in house at Maple Crest and that’s what makes us the best luxury custom home builder in Charlottesville and surrounding areas. We offer the full set of services you need to build your dream home and more. We will exceed your expectations whether we are working with supplied blueprints or designing in house.</p>
    <p>In addition to our custom home building process, we have a wealth of knowledge regarding land available located in our service area. We are also skilled and well versed at working with your pre-owned lot.</p>
  </div>
  <div class="photo" style="left:209px;top:0;width:171px;height:253px;background:linear-gradient(180deg,#dfe3e6 0%,#cfd6dc 35%,#b9c7cf 55%,#9a6a3e 75%,#7d5431 100%)" role="img" aria-label="Photo of a dining room with vaulted beamed ceiling and a wooden farmhouse table"></div>
  <div class="abs orange-block"></div>
  <div class="abs teal-block-b"></div>
  <div class="abs teal-block-a"></div>
  <div class="frame" style="left:22px;top:218px;width:181px;height:137px"></div>
  <div class="photo" style="left:29px;top:226px;width:167px;height:124px;background:linear-gradient(180deg,#eef0f0 0%,#dcdedd 40%,#5a4a40 60%,#6b4a30 80%,#8a6440 100%)" role="img" aria-label="Photo of a kitchen with white cabinets, dark island and wide-plank wood floors"></div>
  <ul class="abs services">
    <li class="has-rule">CUSTOM DESIGN</li>
    <li class="has-rule">ARCHITECTURE</li>
    <li>PROJECT MANAGEMENT</li>
  </ul>
  <p class="abs ideas-quote">Because we are absolutely passionate about the entire home building process you will love it all – from the first scheduled meeting, through the design process, during the construction phase, and eventually handing over the keys to your beautiful new home.</p>
  <div class="folio" style="left:186px;top:504px"><i></i>Page : 04</div>
</section>

</body>
</html>
```